Stationery Design Project

We need a stationery design for a new business consulting business based in New Zealand.
We have the logo and business cards designed and we're looking for letterhead, compliments slip and PowerPoint presentation format that aligns with our business cards.
Industry/Entity Type
Business
Requirements
Must have
- same colors and format as business cards

```html
<!DOCTYPE html>
<html lang="en">
<head>
<meta charset="utf-8">
<title>Tidewell Advisory — Letterhead</title>
<link rel="stylesheet" href="https://fonts.googleapis.com/css2?family=Questrial&display=swap">
<style>
  :root {
    --paper: #ffffff;
    --backdrop: #ffffff;
    --brand-green: #76b52a;
    --bar-grey: #a3a3a3;
    --ink: #2b2b2b;
    --name-grey: #8f8f8f;
  }
  html, body {
    margin: 0;
    padding: 0;
    width: 849px;
    height: 1200px;
    overflow: hidden;
    background: var(--backdrop);
  }
  .letterhead {
    position: relative;
    width: 849px;
    height: 1200px;
    background: var(--paper);
    font-family: "Questrial", "Century Gothic", sans-serif;
    color: var(--ink);
  }
  .side-bar {
    position: absolute;
    left: 0;
    top: 0;
    width: 20px;
    height: 208px;
    background: var(--bar-grey);
  }
  .top-band {
    position: absolute;
    right: 0;
    top: 0;
    width: 391px;
    height: 19px;
    background: var(--brand-green);
  }
  .contact {
    position: absolute;
    left: 80px;
    top: 56px;
    margin: 0;
    font-style: normal;
    font-size: 14px;
    line-height: 21.5px;
  }
  .contact-line {
    display: flex;
    align-items: center;
    height: 21.5px;
  }
  .contact-icon {
    width: 12px;
    height: 12px;
    margin-right: 8px;
    flex: none;
  }
  .brand {
    position: absolute;
    right: 43px;
    top: 101px;
    display: flex;
    align-items: center;
    gap: 12px;
  }
  .brand-dot {
    width: 22px;
    height: 22px;
    border-radius: 50%;
    background: var(--brand-green);
  }
  .brand-name {
    font-size: 38px;
    line-height: 1;
    color: var(--name-grey);
    letter-spacing: -0.5px;
  }
</style>
</head>
<body>
  <main class="letterhead">
    <div class="side-bar"></div>
    <div class="top-band"></div>

    <address class="contact">
      <div class="contact-line">P.O Box 48170</div>
      <div class="contact-line">Wellington 6011 New Zealand</div>
      <div class="contact-line">
        <svg class="contact-icon" viewBox="0 0 12 12" aria-hidden="true">
          <path d="M3 1 L5 3.2 L4 4.6 C4.6 6 5.8 7.3 7.3 8 L8.7 7 L11 9 L9.6 11 C5.5 10.6 1.4 6.5 1 2.4 Z" fill="#76b52a"/>
        </svg>
        + 64 21 555 0142
      </div>
      <div class="contact-line">
        <svg class="contact-icon" viewBox="0 0 12 12" aria-hidden="true">
          <rect x="0.8" y="2.3" width="10.4" height="7.4" fill="none" stroke="#76b52a" stroke-width="1.1"/>
          <path d="M0.8 2.3 L6 6.6 L11.2 2.3" fill="none" stroke="#76b52a" stroke-width="1.1"/>
        </svg>
        hello@tidewelladvisory.com
      </div>
      <div class="contact-line">
        <svg class="contact-icon" viewBox="0 0 12 12" aria-hidden="true">
          <g fill="none" stroke="#76b52a" stroke-width="1">
            <circle cx="6" cy="6" r="5"/>
            <ellipse cx="6" cy="6" rx="2.2" ry="5"/>
            <line x1="1" y1="6" x2="11" y2="6"/>
          </g>
        </svg>
        www.tidewelladvisory.com
      </div>
    </address>

    <div class="brand">
      <span class="brand-dot"></span>
      <span class="brand-name">Tidewell Advisory</span>
    </div>
  </main>
</body>
</html>
```